Ushuaia site

create new design for the site Uhsuaia brevoluz.inf.br
Our benchmark is www.trelmaquest.com
We want a big banner in the center, with huge images as well.
Background must be white.
Must have a sitemap on footer.
Menu "fique por dentro" must be transformed into a horizontal upper menu.
We need: newsletter sign-up field, Pindrel +, Corvalink.
We also need space for ads: square ads in the lateral side, and banners on the upper part.
Please use solely the attached photos to create the layout.

*the current layout is very confusing, something we must fix in the new one.
The vertical menu on the right MUST BE THE HORIZONTAL MENU ON THE TOP ON THE NEW SITE.
The current vertical menu on the left, can either stay vertical on the left, or go to the right, or be transformed into another element, but CAN NEVER BECOME THE PRINCIPAL MENU OF THE SITE ON THE TOP HORIZONTALLY.

*we currently don't have a specific logo, so feel free to create something, but don't worry to elaborate, because we are just a content site as of now.
Since it's a location site, we wouldn't like elements such as planes, passports, etc, associated, because they remind people of travel agencies, which we are not, we are just a destination specialist.
But feel free to use a special font, or some image that associate with Ushuaia, such as mountains, wood signs of the "fin del mundo", etc.

Target Market(s)

travellers who go to Ushuaia and the Patagonia region, and would like to design the tour themselves.

Industry/Entity Type

Travel

Coding

Coded - Design and coding required

Font styles to use
Sans Serif

Colors
ffffff
3176b5
fde08a
0555a3

Requirements
Must have
• * huge banner with images on top for the homepage;
* horizontal menu;
* sign-up for newsletter;
* logos for Pindrel +, and Corvalink;
* footer;
* space for ads.
* We need design for only 3 model pages: homepage, content page, form page (basically the same as content, but with the form).
* html will have to be done for all currently existing pages.
Should not have
• * vomteria logo;
* intranet area.

```html
<!DOCTYPE html>
<html lang="en">
<head>
<meta charset="utf-8">
<title>Brevoluz – Travel guide to Patagonia</title>
<link rel="stylesheet" href="https://fonts.googleapis.com/css2?family=Open+Sans:wght@300;400;700&display=swap">
<style>
  :root {
    --stage: #7d7d7d;
    --white: #ffffff;
    --navy: #0f2f6e;
    --nav-text: #555555;
    --ad-border: #e3ebf3;
    --ad-text: #c3d4e7;
    --ad-small: #c9d3dd;
    --caption-bg: rgba(58, 52, 48, 0.72);
    --hero-top: #c9c3bc;
    --hero-mid: #9a8b7d;
    --hero-bottom: #6f6862;
    --tab-home: #f2c53d;
    --tab-headers: #4aa3df;
    --tab-sliders: #8cc152;
    --tab-features: #e9776b;
    --tab-blog: #5b9bd5;
    --tab-reviews: #a8353a;
    --tab-gallery: #555555;
    --icon: #9a9a9a;
  }
  * { box-sizing: border-box; margin: 0; padding: 0; }
  html, body {
    width: 1200px; height: 765px; overflow: hidden;
    background: var(--stage);
    font-family: "Open Sans", sans-serif;
  }
  .site {
    position: absolute; left: 0; top: 61px;
    width: 1200px; height: 643px;
    background: var(--white);
    overflow: hidden;
  }
  .site-header { position: relative; height: 194px; }
  .brand {
    position: absolute; left: 107px; top: 38px;
    font-size: 50px; font-weight: 700; letter-spacing: 1px;
    color: var(--navy);
  }
  .ad-leaderboard {
    position: absolute; left: 456px; top: 20px;
    width: 650px; height: 80px;
    border: 2px solid var(--ad-border);
  }
  .ad-leaderboard .ad-size {
    position: absolute; left: 0; right: 0; top: 22px;
    text-align: center; font-size: 25px; font-weight: 300;
    color: var(--ad-text); word-spacing: 10px;
  }
  .ad-leaderboard .ad-network {
    position: absolute; left: 20px; top: 52px;
    font-size: 12px; color: var(--ad-small);
  }
  .main-nav {
    position: absolute; left: 107px; top: 138px;
    display: flex; gap: 3px; list-style: none;
  }
  .main-nav li {
    height: 28px; padding-top: 4px;
    text-align: center; font-size: 15px; color: var(--nav-text);
    border-bottom: 3px solid;
  }
  .nav-home { width: 74px; border-color: var(--tab-home) !important; }
  .nav-headers { width: 90px; border-color: var(--tab-headers) !important; }
  .nav-sliders { width: 82px; border-color: var(--tab-sliders) !important; }
  .nav-features { width: 90px; border-color: var(--tab-features) !important; }
  .nav-blog { width: 66px; border-color: var(--tab-blog) !important; }
  .nav-reviews { width: 90px; border-color: var(--tab-reviews) !important; }
  .nav-gallery { width: 84px; border-color: var(--tab-gallery) !important; }
  .search-icon { position: absolute; left: 1091px; top: 146px; }
  .hero {
    position: absolute; left: 0; top: 194px;
    width: 1200px; height: 449px;
    background: linear-gradient(180deg, var(--hero-top) 0%, var(--hero-mid) 55%, var(--hero-bottom) 100%);
  }
  .hero-title {
    position: absolute; left: 96px; top: 138px;
    font-size: 41px; font-weight: 400; line-height: 46px;
    color: var(--white); text-transform: uppercase;
    white-space: nowrap;
  }
  .hero-title span {
    background: var(--caption-bg);
    padding: 0 12px 2px 8px;
    -webkit-box-decoration-break: clone; box-decoration-break: clone;
  }
</style>
</head>
<body>
  <div class="site">
    <header class="site-header">
      <div class="brand">BREVOLUZ</div>
      <div class="ad-leaderboard">
        <div class="ad-size">leaderboard 728 x 90</div>
        <div class="ad-network">plaqora ads</div>
      </div>
      <ul class="main-nav">
        <li class="nav-home">Home</li>
        <li class="nav-headers">Headers</li>
        <li class="nav-sliders">Sliders</li>
        <li class="nav-features">Features</li>
        <li class="nav-blog">Blog</li>
        <li class="nav-reviews">Reviews</li>
        <li class="nav-gallery">Gallery</li>
      </ul>
      <svg class="search-icon" width="14" height="14" viewBox="0 0 14 14" aria-label="Search">
        <circle cx="5.5" cy="5.5" r="4" fill="none" stroke="var(--icon)" stroke-width="2"/>
        <line x1="8.5" y1="8.5" x2="12.5" y2="12.5" stroke="var(--icon)" stroke-width="2.2" stroke-linecap="round"/>
      </svg>
    </header>
    <section class="hero" role="img" aria-label="Photo of sea lions resting on rocks with penguins in the background">
      <h1 class="hero-title"><span>Travel guide to Patagonia , all you need<br>to know for your trip to Ushuaia</span></h1>
    </section>
  </div>
</body>
</html>
```